Unique and original Business Card for Financial Services Business

I have moved premises and need to change the detail on my business card so thought now is a good time for a re-design. Looking for something professional and modern with colours to fit in with out logo. Like the idea of foil or embossing if that works but not a must have but I do want something that stands out and that I could not design myself.

Once business card is designed I will also be looking to get letterhead and flyers done but want the business card concept in place first.

The majority of designs I am receiving are generic and template based. I am looking for something unique and original. We have some great design elements in our logo, think outside the box and show me something that stands out from the crowd.

Target Market(s)

Business Professionals

Industry/Entity Type

Finance

Contact Information for Business Card

Name: Delia Norwood Phone 0473 958 162 Address PO Box 8617 Mossvale NSW 2389 Email info@steadyharbourfinancialservices.com.au website www.steadyharbourfinancialservices.com.au

Font styles to use
Other font styles liked:
• Ralway

Requirements
Should not have
• No black backgrounds please

```html
<!DOCTYPE html>
<html lang="en">
<head>
<meta charset="utf-8">
<title>Steady Harbour Financial Services – Business Card</title>
<link href="https://fonts.googleapis.com/css2?family=Raleway:wght@300;400&display=swap" rel="stylesheet">
<style>
  :root {
    --page: #fdfdfd;
    --card: #f0f0f0;
    --teal: #038f93;
    --ink: #444444;
    --white: #ffffff;
  }
  html, body {
    margin: 0;
    padding: 0;
    width: 1200px;
    height: 1200px;
    overflow: hidden;
    background: var(--page);
    font-family: "Raleway", sans-serif;
  }
  .business-card {
    position: absolute;
    left: 232px;
    top: 400px;
    width: 718px;
    height: 386px;
    background: var(--card);
    overflow: hidden;
  }
  .card-wave {
    position: absolute;
    inset: 0;
  }
  .brand-mark {
    position: absolute;
    left: 318px;
    top: 50px;
    width: 82px;
    height: 82px;
    border-radius: 50%;
    background: var(--teal);
  }
  .brand-name {
    position: absolute;
    left: 0;
    width: 100%;
    margin: 0;
    text-align: center;
    color: var(--teal);
    font-weight: 300;
    line-height: 1;
  }
  .brand-name__main {
    top: 146px;
    font-size: 38px;
    letter-spacing: 0.5px;
  }
  .brand-name__sub {
    top: 184px;
    font-size: 19px;
    letter-spacing: 10.5px;
    padding-left: 10px;
  }
  .contact-list {
    position: absolute;
    left: 0;
    top: 288px;
    width: 100%;
    margin: 0;
    padding: 0;
    list-style: none;
    color: var(--white);
    font-weight: 400;
    font-size: 20px;
    letter-spacing: 1px;
    text-align: center;
  }
  .contact-list li {
    height: 22px;
    line-height: 22px;
  }
  .contact-list .contact-web {
    margin-top: 3px;
    display: flex;
    justify-content: center;
    align-items: center;
    gap: 8px;
    padding-right: 8px;
  }
  .contact-icon {
    width: 20px;
    height: 26px;
    background: var(--white);
    border-radius: 40% 10% 40% 10%;
  }
</style>
</head>
<body>
  <div class="business-card">
    <svg class="card-wave" width="718" height="386" viewBox="0 0 718 386" aria-hidden="true">
      <path fill="var(--teal)" d="M0,260 C40,285 80,292 117,291 C200,290 300,220 364,218 C430,216 460,298 540,300 C610,302 680,275 718,261 L718,386 L0,386 Z"/>
    </svg>

    <div class="brand-mark" aria-hidden="true"></div>
    <p class="brand-name brand-name__main">STEADY HARBOUR</p>
    <p class="brand-name brand-name__sub">Financial Services</p>

    <ul class="contact-list">
      <li>XXX XXXX XX</li>
      <li>XXX XXXX XX</li>
      <li class="contact-web">
        <span class="contact-icon" role="img" aria-label="Small bird silhouette icon"></span>
        <span>XXXXXXXXXXXXXX</span>
      </li>
    </ul>
  </div>
</body>
</html>
```